Brightholm painting

Am looking for a lawn sign design for my paintings company.
I also attached my business card a example

Phone number of the business +1(431)572-8846
Key words:Free estimates|pressure washing |Residential| Commercial | Interior | Exterior

```html
<!DOCTYPE html>
<html lang="en">
<head>
<meta charset="utf-8">
<title>Brightholm Painting – Lawn Sign</title>
<link rel="stylesheet" href="https://fonts.googleapis.com/css2?family=Jost:wght@500;600;700&display=swap">
<style>
  :root {
    --backdrop: #8a8a8a;
    --ink: #000000;
    --paper: #ffffff;
    --sky: #1eaae1;
  }
  html, body {
    margin: 0;
    width: 1200px;
    height: 944px;
    overflow: hidden;
    background: var(--backdrop);
  }
  .lawn-sign {
    position: absolute;
    left: 0;
    top: 22px;
    width: 1200px;
    height: 900px;
    display: block;
  }
  .band-header { fill: var(--ink); }
  .band-services { fill: var(--sky); }
  .band-contact { fill: var(--paper); }
  .brand-name {
    font-family: "Jost", sans-serif;
    font-weight: 500;
    font-size: 220px;
    fill: var(--sky);
  }
  .service-list {
    font-family: "Jost", sans-serif;
    font-weight: 700;
    font-size: 72px;
    fill: var(--ink);
  }
  .estimate-pill { fill: var(--ink); }
  .estimate-label {
    font-family: "Jost", sans-serif;
    font-weight: 600;
    font-size: 94px;
    fill: var(--sky);
  }
  .phone-badge { fill: var(--sky); }
  .phone-icon { fill: var(--ink); }
  .phone-waves { fill: none; stroke: var(--ink); stroke-width: 5; stroke-linecap: round; }
  .phone-number {
    font-family: "Jost", sans-serif;
    font-weight: 600;
    font-size: 132px;
    fill: var(--ink);
  }
</style>
</head>
<body>
<svg class="lawn-sign" viewBox="0 0 1200 900" xmlns="http://www.w3.org/2000/svg" role="group" aria-label="Brightholm Painting lawn sign">
  <rect class="band-contact" x="0" y="0" width="1200" height="900"/>
  <rect class="band-header" x="0" y="0" width="1200" height="444"/>
  <rect class="band-services" x="0" y="444" width="1200" height="234"/>

  <text class="brand-name" x="60" y="194" textLength="1083" lengthAdjust="spacingAndGlyphs">BRIGHTHOLM</text>
  <text class="brand-name" x="159" y="397" textLength="890" lengthAdjust="spacingAndGlyphs">PAINTING</text>

  <text class="service-list" x="71" y="525" textLength="1058" lengthAdjust="spacingAndGlyphs">PRESSURE WASHING | RESIDENTIAL</text>
  <text class="service-list" x="39" y="602" textLength="1084" lengthAdjust="spacingAndGlyphs">COMMERCIAL | INTERIOR | EXTERIOR</text>

  <rect class="estimate-pill" x="269" y="639" width="660" height="89" rx="44.5"/>
  <text class="estimate-label" x="328" y="706" textLength="543" lengthAdjust="spacingAndGlyphs">FREE ESTIMATES</text>

  <g class="phone-mark">
    <circle class="phone-badge" cx="99" cy="807" r="50"/>
    <path class="phone-icon" d="M80 782c3-3 7-3 9 0l7 10c2 3 1 6-1 8l-4 3c3 7 9 13 16 17l3-4c2-2 5-3 8-1l10 7c3 2 3 6 0 9l-5 5c-4 4-11 4-18 0-12-7-22-17-29-29-4-7-4-14 0-18z"/>
    <path class="phone-waves" d="M104 790a12 12 0 0 1 11 11"/>
    <path class="phone-waves" d="M106 779a22 22 0 0 1 20 20"/>
  </g>
  <text class="phone-number" x="177" y="849" textLength="973" lengthAdjust="spacingAndGlyphs">+1(431) 572-8846</text>
</svg>
</body>
</html>
```